Antigen Preservation Center

The company will provide a contract research services to stabilize various viruses, viral vectors, and vaccines. It may offer some licensing opportunities for stabilizing technologies. Main area of applications are pharmaceutical, therapeutic, and vaccination field. The company aspires to develop room temperature vaccines for global distribution beyond the current cold chain.
Updates

Target Market(s)

pharmaceutical, therapeutic and vaccination fields

Coding

Number of Pages Required

4 page

Requirements
Must have
• Incorporate a APC logo, attached at the bottom, on the Web page

```html
<!DOCTYPE html>
<html lang="en">
<head>
<meta charset="utf-8">
<title>Antigen Preservation Center</title>
<link href="https://fonts.googleapis.com/css2?family=Montserrat:wght@300;400;600;700&family=Open+Sans:wght@400;600&display=swap" rel="stylesheet">
<style>
:root{
  --teal:#5a9e86;
  --teal-dark:#3f7f69;
  --ink:#2b2b2b;
  --muted:#8a8a8a;
  --line:#d9d9d9;
  --white:#ffffff;
  --footer:#1d1d1d;
  --footer-deep:#121212;
  --hero-a:#3d6e8c;
  --hero-b:#9cc3cf;
}
*{box-sizing:border-box;margin:0;padding:0}
html,body{width:1200px;height:5248px;overflow:hidden}
body{font-family:"Open Sans",Arial,sans-serif;color:var(--ink);background:var(--white);font-size:14px}
.section{position:relative;width:1200px;overflow:hidden}
.wrap{width:1000px;margin:0 auto;position:relative}
.title{font-family:"Montserrat",sans-serif;font-weight:600;font-size:32px;text-align:center;color:var(--ink)}
.divider{display:flex;align-items:center;justify-content:center;gap:14px;margin:14px auto 26px;width:1000px}
.divider span{flex:1;height:1px;background:var(--line)}
.light .title{color:var(--white)}
.light .divider span{background:rgba(255,255,255,.45)}
.copy{font-size:14px;line-height:24px;color:var(--muted);text-align:center;width:980px;margin:0 auto}
.light .copy{color:rgba(255,255,255,.92)}
.btn{display:inline-block;font-family:"Montserrat",sans-serif;font-size:11px;font-weight:600;letter-spacing:1px;padding:7px 20px;border:2px solid var(--ink);color:var(--ink);background:var(--white)}
.center{text-align:center}

/* hero */
.hero{height:682px;background:linear-gradient(100deg,var(--hero-a) 0%,#5f93a8 45%,var(--hero-b) 100%)}
.nav{position:absolute;top:0;left:0;right:0;height:100px;display:flex;align-items:center;justify-content:space-between;padding:0 115px 0 130px;z-index:2}
.brand{display:flex;align-items:center;gap:12px;color:var(--white);font-family:"Montserrat",sans-serif;font-weight:600;font-size:13px;letter-spacing:2px;line-height:17px}
.brand i{width:28px;height:28px;border:2px solid var(--white);display:block}
.menu{display:flex;gap:24px;font-family:"Montserrat",sans-serif;font-size:12px;font-weight:600;color:var(--white);letter-spacing:.5px}
.hero-copy{position:absolute;top:245px;left:0;right:0;text-align:center;color:var(--white)}
.hero-copy h1{font-family:"Montserrat",sans-serif;font-weight:300;font-size:52px;line-height:60px}
.hero-copy p{font-family:"Montserrat",sans-serif;font-size:11px;letter-spacing:2px;margin:10px 0 24px}
.hero-copy .btn{background:transparent;border-color:var(--white);color:var(--white)}
.dots{position:absolute;top:615px;left:0;right:0;display:flex;justify-content:center;gap:8px}
.dots b{width:8px;height:8px;border-radius:50%;background:rgba(255,255,255,.5)}
.dots b:first-child{background:var(--white)}

/* about */
.about{height:438px;padding-top:58px}
.about .copy+.copy{margin-top:22px}
.about .btn{margin-top:30px}

/* team */
.team{height:553px;background:var(--teal);padding-top:50px}
.team-photo{position:absolute;left:130px;right:130px;bottom:0;height:310px;background:linear-gradient(180deg,rgba(255,255,255,.08),rgba(255,255,255,.35))}

/* contact */
.contact{height:584px;padding-top:60px}
.form{display:flex;justify-content:space-between;width:950px;margin:0 auto}
.col{width:400px}
.field{font-size:12px;color:var(--muted);margin-bottom:6px}
.field em{color:#c0392b;font-style:normal}
.input{height:38px;border:1px solid #bbb;margin-bottom:26px}
.area{height:132px;border:1px solid #bbb}
.check{display:flex;align-items:center;gap:8px;font-size:12px;color:var(--muted);margin-top:8px}
.check i{width:14px;height:14px;border:1px solid #999;display:block}
.contact .center{margin-top:30px}

/* research */
.research{height:665px;background:linear-gradient(180deg,#1f5c3a 0%,#2f8a4c 45%,#a9d4a2 78%,#ffffff 100%);padding-top:55px}
.research .btn{margin-top:30px;background:transparent;border-color:var(--white);color:var(--white)}
.research-art{position:absolute;left:300px;top:400px;width:620px;height:240px;border-radius:120px;background:linear-gradient(90deg,rgba(240,230,170,.7),rgba(120,190,230,.65))}

/* blog */
.blog{height:568px;padding-top:55px}
.cards{display:flex;justify-content:center;gap:32px}
.card{width:272px}
.card-img{height:185px;background:linear-gradient(135deg,#7f9fb6,#cdd9e2)}
.card:nth-child(2) .card-img{background:linear-gradient(135deg,#9ab4c8,#e2d4c9)}
.card:nth-child(3) .card-img{background:linear-gradient(135deg,#c98a6a,#7a5b4d)}
.card h3{font-family:"Montserrat",sans-serif;font-size:15px;font-weight:700;letter-spacing:1px;margin:18px 0 6px}
.meta{font-size:11px;color:var(--muted)}
.card p{font-size:12px;line-height:18px;color:var(--muted);margin:10px 0 16px}
.more{font-family:"Montserrat",sans-serif;font-size:11px;font-weight:700;color:var(--teal)}
.arrow{position:absolute;top:325px}

/* join */
.join{height:507px;background:linear-gradient(180deg,#7ea9c2 0%,#aecbdb 50%,#dfe9ee 100%);padding-top:58px}
.join .btn{margin-top:30px;background:transparent;border-color:var(--white);color:var(--white)}

/* newsletter */
.news{height:385px;padding-top:58px}
.sub{display:flex;justify-content:center;margin-top:34px}
.sub .input{width:400px;height:34px;margin:0;font-size:12px;color:var(--muted);padding:8px 12px}
.sub .go{background:var(--teal);color:var(--white);font-family:"Montserrat",sans-serif;font-size:11px;font-weight:700;letter-spacing:1px;padding:10px 22px;margin-left:10px}

/* map */
.map{height:458px;background:linear-gradient(135deg,#e7e4dc,#d6dcd2 55%,#e9e6df)}

/* footer */
.footer{height:357px;background:var(--footer);color:#d0d0d0;padding:48px 0 0 85px;display:flex;gap:60px}
.footer h4{font-family:"Montserrat",sans-serif;font-size:17px;font-weight:600;color:var(--white);margin-bottom:20px;letter-spacing:.5px}
.f-brand{width:240px}
.f-brand .brand{margin-bottom:24px}
.f-brand p{font-size:12px;line-height:18px}
.f-contact{width:210px;font-size:12px;line-height:18px}
.f-row{display:flex;gap:14px;margin-bottom:14px}
.f-links{width:200px;font-size:13px;line-height:19px;color:var(--white)}
.f-form{width:300px}
.f-form .pair{display:flex;gap:8px}
.f-form .in{flex:1;height:34px;background:var(--white);color:#777;font-size:12px;padding:9px 10px;margin-bottom:8px}
.f-form .send{width:130px;height:34px;background:var(--teal);color:var(--white);font-family:"Montserrat",sans-serif;font-size:12px;font-weight:700;text-align:center;line-height:34px}
.copyright{height:51px;background:var(--footer-deep);color:#8e8e8e;font-size:11px;text-align:center;line-height:51px}
</style>
</head>
<body>

<header class="section hero">
  <div role="img" aria-label="Photo of a scientist in a laboratory working with vials" style="position:absolute;inset:0"></div>
  <nav class="nav">
    <div class="brand"><i></i><div>ANTIGEN<br>PRESERVATION<br>CENTER</div></div>
    <div class="menu"><span>HOME</span><span>ABOUT ▾</span><span>TEAM ▾</span><span>RESEARCH ▾</span><span>CONTACT ▾</span><span>JOIN TEAM ▾</span></div>
  </nav>
  <div class="hero-copy">
    <h1>Developing<br>room temperature vaccines</h1>
    <p>FOR GLOBAL DISTRIBUTION BEYOND THE CURRENT COLD CHAIN</p>
    <span class="btn">FIND MORE INFO</span>
  </div>
  <div class="dots"><b></b><b></b><b></b></div>
</header>

<section class="section about">
  <h2 class="title">About Us</h2>
  <div class="divider"><span></span><svg width="20" height="20" viewBox="0 0 20 20"><circle cx="10" cy="10" r="6" fill="none" stroke="#bbb" stroke-width="1.5"/></svg><span></span></div>
  <p class="copy">Lorem ipsum dolor sit amet, consectetur adipiscing elit. Duis autem nobis admissionis, cum propius accessisset? At hoc usque quaque, aliter in vita? Vestigium terra animale, sed de ceteris imperite quaerimus, quale in dolor nobis efficitur voluptatem, ese non ipsum in possessio sapiens fauget eum possunt. Huic mihi optimum esse propter desperationem sapientiae, illi propter spem vivere. Quid enim me prohiberet Epicureum esse, si probarem, quae ille diceret? Qui vero illustris, quamvis molestius simus sicuti es plenaria.</p>
  <p class="copy">Videbatur autem si quicumque intuere istius veteres philosophiae et animadverte, nobis est nos superabat. Et quos ea mutus, quod apud sapientes? Fuit nihil cursum dei quamque; rerum istam tamen nihil et cur est ipsa?</p>
  <div class="center"><span class="btn">MORE DETAILS →</span></div>
</section>

<section class="section team light">
  <h2 class="title">Our Team</h2>
  <div class="divider"><span></span><svg width="20" height="20" viewBox="0 0 20 20"><circle cx="10" cy="10" r="6" fill="none" stroke="#fff" stroke-width="1.5"/></svg><span></span></div>
  <p class="copy">Lorem ipsum dolor sit amet, consectetur adipiscing elit. Duis autem nobis admissionis, cum propius accessisset? At hoc usque quaque, aliter in vita? Non igitur de improbo, sed de callido improbo quaerimus, quale in dolor.</p>
  <div class="team-photo" role="img" aria-label="Photo of five doctors in white coats standing in a row"></div>
</section>

<section class="section contact">
  <h2 class="title">Contact Us</h2>
  <div class="divider"><span></span><svg width="20" height="20" viewBox="0 0 20 20"><circle cx="10" cy="10" r="6" fill="none" stroke="#bbb" stroke-width="1.5"/></svg><span></span></div>
  <div class="form">
    <div class="col">
      <div class="field">Name <em>*</em></div><div class="input"></div>
      <div class="field">Email <em>*</em></div><div class="input"></div>
      <div class="field">Phone</div><div class="input"></div>
    </div>
    <div class="col">
      <div class="field">Description</div><div class="area"></div>
      <div class="field" style="margin-top:22px">Required</div>
      <div class="check"><i></i>I have read the Disclaimer and Privacy Policy</div>
    </div>
  </div>
  <div class="center"><span class="btn">SUBMIT</span></div>
</section>

<section class="section research light">
  <div role="img" aria-label="Background image of green DNA strands" style="position:absolute;inset:0"></div>
  <h2 class="title" style="position:relative">Research</h2>
  <div class="divider" style="position:relative"><span></span><svg width="20" height="20" viewBox="0 0 20 20"><circle cx="10" cy="10" r="6" fill="none" stroke="#fff" stroke-width="1.5"/></svg><span></span></div>
  <p class="copy" style="position:relative">Lorem ipsum dolor sit amet, consectetur adipiscing elit. Duis autem nobis admissionis, cum propius accessisset? At hoc usque quaque, aliter in vita? Vestigium terra animale, sed de ceteris imperite quaerimus, quale in dolor nobis efficitur voluptatem, ese non ipsum in possessio sapiens fauget eum possunt. Huic mihi optimum esse propter desperationem sapientiae, illi propter spem vivere.</p>
  <div class="center" style="position:relative"><span class="btn">MORE DETAILS →</span></div>
  <div class="research-art" role="img" aria-label="Image of a vaccine vial and a syringe"></div>
</section>

<section class="section blog">
  <h2 class="title">Blog Post</h2>
  <div class="divider"><span></span><svg width="20" height="20" viewBox="0 0 20 20"><circle cx="10" cy="10" r="6" fill="none" stroke="#bbb" stroke-width="1.5"/></svg><span></span></div>
  <svg class="arrow" style="left:62px" width="20" height="40" viewBox="0 0 20 40"><path d="M16 2 L4 20 L16 38" fill="none" stroke="#ccc" stroke-width="2"/></svg>
  <svg class="arrow" style="right:62px" width="20" height="40" viewBox="0 0 20 40"><path d="M4 2 L16 20 L4 38" fill="none" stroke="#ccc" stroke-width="2"/></svg>
  <div class="cards">
    <article class="card">
      <div class="card-img" role="img" aria-label="Photo of a laboratory microscope"></div>
      <h3>LOREM IPSUM DOLOR SIT AMET</h3>
      <div class="meta">May 26, 2017 | <b>ADMIN</b> | Uncategorized</div>
      <p>Lorem ipsum dolor sit amet, consectetur adipiscing elit. Duis autem nobis admissionis.</p>
      <span class="more">CONTINUE →</span>
    </article>
    <article class="card">
      <div class="card-img" role="img" aria-label="Photo of a medical team meeting"></div>
      <h3>LOREM IPSUM DOLOR SIT AMET</h3>
      <div class="meta">May 26, 2017 | <b>ADMIN</b> | Uncategorized</div>
      <p>Lorem ipsum dolor sit amet, consectetur adipiscing elit. Duis autem nobis admissionis.</p>
      <span class="more">CONTINUE →</span>
    </article>
    <article class="card">
      <div class="card-img" role="img" aria-label="Photo of a child receiving a vaccination"></div>
      <h3>LOREM IPSUM DOLOR SIT AMET</h3>
      <div class="meta">May 26, 2017 | <b>ADMIN</b> | Uncategorized</div>
      <p>Lorem ipsum dolor sit amet, consectetur adipiscing elit. Duis autem nobis admissionis.</p>
      <span class="more">CONTINUE →</span>
    </article>
  </div>
</section>

<section class="section join light">
  <div role="img" aria-label="Photo of clasped hands" style="position:absolute;inset:0"></div>
  <h2 class="title" style="position:relative">Join Team</h2>
  <div class="divider" style="position:relative"><span></span><svg width="20" height="20" viewBox="0 0 20 20"><circle cx="10" cy="10" r="6" fill="none" stroke="#fff" stroke-width="1.5"/></svg><span></span></div>
  <p class="copy" style="position:relative">Lorem ipsum dolor sit amet, consectetur adipiscing elit. Duis autem nobis admissionis, cum propius accessisset? At hoc usque quaque, aliter in vita? Vestigium terra animale, sed de ceteris imperite quaerimus, quale in dolor nobis efficitur voluptatem, ese non ipsum in possessio sapiens fauget eum possunt. Huic mihi optimum esse propter desperationem sapientiae, illi propter spem vivere.</p>
  <p class="copy" style="position:relative;margin-top:22px">Videbatur autem si quicumque intuere istius veteres philosophiae et animadverte, nobis est nos superabat. Et quos ea mutus, quod apud sapientes? Fuit nihil cursum dei quamque; rerum istam tamen nihil et cur est ipsa? Quid enim me prohiberet esse, si probarem?</p>
  <div class="center" style="position:relative"><span class="btn">JOIN NOW</span></div>
</section>

<section class="section news">
  <h2 class="title">Newsletter Signup</h2>
  <div class="divider"><span></span><svg width="20" height="20" viewBox="0 0 20 20"><circle cx="10" cy="10" r="6" fill="none" stroke="#bbb" stroke-width="1.5"/></svg><span></span></div>
  <p class="copy">Lorem ipsum dolor sit amet, consectetur adipiscing elit. Duis autem nobis admissionis, cum propius accessisset? At hoc usque quaque, aliter in vita? Vestigium terra animale, sed de ceteris imperite quaerimus, quale in dolor nobis efficitur voluptatem. Huic mihi optimum esse propter desperationem sapientiae, illi propter spem vivere.</p>
  <div class="sub"><div class="input">Enter Your Email</div><span class="go">SUBSCRIBE</span></div>
</section>

<section class="section map" role="img" aria-label="Road map of the region with a location pin"></section>

<footer class="section footer">
  <div class="f-brand">
    <div class="brand"><i></i><div>ANTIGEN<br>PRESERVATION<br>CENTER</div></div>
    <p>Lorem ipsum dolor sit amet, non veniens adipiscing elit. Morbi autem admissiones semper. Ras tellus quis lacus quis ante vivamus lorem tincidunt.</p>
  </div>
  <div class="f-contact">
    <h4>CONTACT US</h4>
    <div class="f-row"><svg width="14" height="18" viewBox="0 0 14 18"><path d="M7 1a6 6 0 0 0-6 6c0 4.5 6 10 6 10s6-5.5 6-10a6 6 0 0 0-6-6z" fill="#fff"/><circle cx="7" cy="7" r="2.2" fill="#1d1d1d"/></svg><div>418 Linden Ave<br>Fairview TX 75069</div></div>
    <div class="f-row"><svg width="14" height="16" viewBox="0 0 14 16"><path d="M3 1h3l1 4-2 1.5c.8 2 2 3.2 3.5 3.5L10 8l4 1v3c0 1-1 2-2 2C6 14 1 9 1 3c0-1 1-2 2-2z" fill="#fff"/></svg><div>555.014.2290</div></div>
    <div class="f-row"><svg width="14" height="12" viewBox="0 0 14 12"><rect x=".5" y="1" width="13" height="10" fill="#fff"/><path d="M1 1.5l6 5 6-5" fill="none" stroke="#1d1d1d" stroke-width="1.2"/></svg><div>hello@apc-lab.com</div></div>
  </div>
  <div class="f-links">
    <h4>ABOUT US</h4>
    <div>Home</div><div>About</div><div>Team</div><div>Research</div><div>Contact</div><div>Join Team</div>
  </div>
  <div class="f-form">
    <h4>GET IN TOUCH</h4>
    <div class="pair"><div class="in">Name</div><div class="in">Phone</div></div>
    <div class="pair"><div class="in">Email address</div></div>
    <div class="send">SEND</div>
  </div>
</footer>
<div class="copyright">Copyright © 2017 antigenpreservation.com · All Rights Reserved</div>

</body>
</html>
```